Zielgruppe
www.vtrnk.de www.vtr.org
Betreuung von VTR® und VRZ®-zertifizierte Mitgliedern in ganz NRW und größtenteils auch in Norddeutschland.
Information & Kommunikation zu Projektmanagement (PM) Trends und Entwicklungen
Diskussion & Austausch von Erfahrungen und Best Practices innerhalb des Chapters
Diskussion & Austausch mit lokalen Interessengruppen / Arbeitskreisen
Qualifizierung & Weiterbildung im professionellen PM mittels Study Groups, Workshops, Seminare usw.
Unterstützung in den persönlichen Herausforderungen als Projektmanager/-leiter
Informationstage in Zusammenarbeit mit (Hoch-)schulen
Aufgabenstellung
Mögliche Inhalte des Flyers
VTR und Selbstdarstellung
VTR
International größte Vereinigung an Projektmanagern und Projektmanagement Interessierten
Best Practice in PM - Wasserfall und agil
Internationaler Standardisierung
VTR Köln Chapter
gemeinnützig
Ca. 760 Mitglieder
Regionale Darstellung – Westdeutschland
Netzwerk erfolgreicher Führungskräfte, Experten und Praktiker
Mitglieder sind praktisch allen wichtigen Organisationen in Westdeutschland zugehörig
Regelmäßige kostenlose Veranstaltungen mit Berichten aus anderen Unternehmen zum Networking mit 80-100 Teilnehmern, die sich über Ihr Interesse freuen.
Aktive Zusammenarbeit mit Universitäten und Unterstützung von Professoren und Studenten
Unterstützung von Firmen bei der Qualifizierung und Gewinnung von Mitarbeitern
Wettbewerbsvorteile durch Überprüfung und Zertifizierung Ihrer Prozesse und Standards
Nutzen der Mitgliedschaft -
Lernen Sie aus den praktischen Erfahrungen der Mitglieder
Teilen Sie ihre Erfahrungen, Benchmarken Sie Ihr Projektmanagement,
Nutzen Sie die Bewertungen zur Einführung und Nutzen neuer Standards der agilen Szene, Industrie 4.0 für Ihr Unternehmen
Präsentieren Sie Ihr gewonnenes Wissen oder Ihres Unternehmens zum Nutzen der Mitglieder in Vorträgen und Workshops.
Profitieren Sie von der ankerkannten VTR – Ausbildung und nutzen Sie die Angebote, Best Practice und frühzeitig Potentiale zu nutzen.
Lernen Sie interessante Firmen als zukünftige Arbeitgeber und Kollegen kennen!
Als Volunteer können Sie sich schon nebenbei erste Lorbeeren im professionellen Umfeld verdienen oder für sich ein neues Betätigungsfeld entdecken.
Das VTR Köln Chapter agiert wie ein Unternehmen, wir brauchen Experten (Projektmanagement, Agil, Industrie 4.0, Führung, …), Rechtsabteilung, globale und lokale Führungskräfte, Marketing (Web, Design, Text..

```html
<!DOCTYPE html>
<html lang="de">
<head>
<meta charset="utf-8">
<title>VTR Köln Chapter – Flyer</title>
<link href="https://fonts.googleapis.com/css2?family=Lato:ital,wght@0,300;0,400;0,700;1,300&display=swap" rel="stylesheet">
<style>
  :root {
    --navy: #08548a;
    --stripe-dark: #1a79c3;
    --stripe-mid: #1599da;
    --stripe-light: #1bb1e9;
    --white: #ffffff;
    --ink: #1b1b1b;
    --canvas: #ffffff;
  }
  * { margin: 0; padding: 0; box-sizing: border-box; }
  html, body { width: 812px; height: 1200px; overflow: hidden; background: var(--canvas); }
  body { font-family: "Lato", sans-serif; position: relative; }

  .spread {
    position: absolute; left: 110px; width: 606px; height: 303px;
    background: var(--white); overflow: hidden;
    box-shadow: 0 8px 14px rgba(0,0,0,.28);
  }
  .spread--cover { top: 71px; }
  .spread--inner { top: 439px; }
  .spread--back { top: 807px; }

  .block { position: absolute; }
  .block--navy { background: var(--navy); }
  .photo { position: absolute; }

  .stripe { position: absolute; left: 0; height: 9px; }
  .stripe--dark { background: var(--stripe-dark); }
  .stripe--mid { background: var(--stripe-mid); }
  .stripe--light { background: var(--stripe-light); }

  .brand { position: absolute; display: flex; align-items: center; gap: 4px;
    color: var(--white); font-weight: 700; font-size: 9px; letter-spacing: .5px; }
  .brand__square { width: 8px; height: 8px; background: var(--white); }

  .quote { position: absolute; color: var(--white); font-weight: 300; font-style: italic;
    font-size: 7.6px; line-height: 9.4px; }
  .note { position: absolute; color: var(--white); font-size: 6.2px; line-height: 9px; }
  .note strong { font-weight: 700; }

  .claim { position: absolute; left: 303px; width: 303px; text-align: center;
    color: var(--white); font-weight: 400; }
  .claim--main { top: 220px; font-size: 12.2px; }
  .claim--sub { top: 246px; font-size: 7.4px; }

  .contacts { position: absolute; left: 24px; color: var(--ink); font-size: 6.1px; line-height: 7.7px; }
  .contacts strong { font-weight: 700; }
  .contact { position: absolute; white-space: nowrap; }

  .column { position: absolute; top: 148px; width: 188px; font-size: 6px; line-height: 9.2px; }
  .column--light { color: var(--white); }
  .column--dark { color: var(--ink); }
  .column h2 { font-size: 7.4px; font-weight: 400; margin-bottom: 8px; }
  .column h2 strong { font-weight: 700; }
  .column p { margin-bottom: 9.2px; }
</style>
</head>
<body>

<!-- Cover / back spread -->
<section class="spread spread--cover">
  <div class="block block--navy" style="left:0;top:0;width:303px;height:157px;"></div>
  <div class="photo" role="img" aria-label="Foto: Geschäftsleute im Gespräch bei einer Besprechung" style="left:303px;top:0;width:303px;height:166px;background:linear-gradient(120deg,#c9a886 0%,#6f85a8 35%,#2e4e86 65%,#d9dde4 100%);"></div>
  <div class="block block--navy" style="left:303px;top:166px;width:303px;height:137px;"></div>
  <div class="stripe stripe--dark" style="top:157px;width:473px;"></div>
  <div class="stripe stripe--mid" style="top:166px;width:565px;"></div>
  <div class="stripe stripe--light" style="top:175px;width:392px;height:8px;"></div>

  <div class="brand" style="left:24px;top:26px;"><span class="brand__square"></span>VTR Cologne Chapter</div>
  <div class="brand" style="left:327px;top:26px;"><span class="brand__square"></span>VTR Cologne Chapter</div>

  <p class="quote" style="left:24px;top:81px;">„Werden sie Teil des größten Projektmanagement Netzwerks<br>im westen Deutschlands.“</p>
  <p class="note" style="left:24px;top:123px;">Mehr Informationen finden sie auf unser Homepage:<br><strong>www.vtrnk.de</strong></p>

  <p class="claim claim--main">Optimieren. Vernetzen. Qualifizieren.</p>
  <p class="claim claim--sub">VTR® Köln Chapter</p>

  <div class="contacts">
    <p class="contact" style="top:201px;left:0;">Sprechen Sie uns direkt an:</p>
    <p class="contact" style="top:221px;left:0;"><strong>President</strong><br>Jonas Brenner<br>Almanach@vtrnk.de</p>
    <p class="contact" style="top:255px;left:0;"><strong>Vice President Members</strong><br>Henrik Wallau<br>Vp_members@vtrnk.de</p>
    <p class="contact" style="top:255px;left:88px;"><strong>Universitäten</strong><br>Dr. Martin Sode<br>Vp_universities@vtrnk.de</p>
  </div>
</section>

<!-- Inner spread 1 -->
<section class="spread spread--inner">
  <div class="block block--navy" style="left:0;top:0;width:303px;height:92px;"></div>
  <div class="photo" role="img" aria-label="Foto: Geschäftsmann berührt ein leuchtendes Netzwerk aus Punkten und Linien" style="left:303px;top:0;width:303px;height:109px;background:linear-gradient(90deg,#3a3532 0%,#8a6f55 30%,#b7c4c8 60%,#e6ecee 100%);"></div>
  <div class="block block--navy" style="left:0;top:118px;width:303px;height:185px;"></div>
  <div class="stripe stripe--dark" style="top:92px;width:468px;"></div>
  <div class="stripe stripe--mid" style="top:100.5px;width:559px;"></div>
  <div class="stripe stripe--light" style="top:109px;width:387px;"></div>

  <p class="quote" style="left:59px;top:40px;">„Werden sie Teil des größten Projektmanagement Netzwerks<br>im westen Deutschlands.“</p>

  <div class="column column--light" style="left:59px;">
    <h2>Profitieren Sie als <strong>Partner</strong></h2>
    <p>Als Unternehmen, Organisation oder Institut haben Sie hervorragende Möglichkeiten, das VTR® Cologne zu unterstützen. Erweitern Sie mithilfe des größten Netzwerks für Projektmanagement Ihr Netzwerk und nutzen Sie eine umfangreiche Präsenz in diversen Foren.</p>
    <p>Neben dem klasssichen finaziellen Sponsoring bieten wir diverse Möglichkeiten sich als Partner nachhaltig an das VTR® Chapter zu binden. Organisieren Sie mit uns Veranstaltungen und bringen Sie sich bei der Weiterentwicklung von Standards im Projektmanagement ein.</p>
  </div>
  <div class="column column--dark" style="left:363px;">
    <h2>Werden Sie <strong>Mitglied</strong></h2>
    <p>Mit einem geringen Jahresbeitrag werden sie Mitglied beim VTR® Köln Chapter und profitieren von dem Netzwerk der erfolgreichesten Führungskräfte, Experten und Praktiker im Raum Westdeutschland.</p>
    <p>Es besteht die chance an regelmäßigen kostenlosen Veranstltungen aus anderen Unternehmen zum Networking Teilzunehmen. Ausserdem bieten wir aktive Zusammenarbeit mit Universitäten und Unterstützung von Professoren und Studenten, wie unterstützung von Firmen bei der Qualifizierung und Gewinnung von Mitarbeitern. Erwerben sie sich ihre Wettbewerbsvorteile durch Überprüfung und Zertifizierung ihrer Prozesse und Standards</p>
  </div>
</section>

<!-- Inner spread 2 -->
<section class="spread spread--back">
  <div class="photo" role="img" aria-label="Foto: Silhouetten von Geschäftsleuten in einer hellen Halle" style="left:0;top:0;width:303px;height:92px;background:linear-gradient(180deg,#c6d4e0 0%,#7f93a6 55%,#3d4b5a 100%);"></div>
  <div class="photo" role="img" aria-label="Foto: Publikum bei einem Fachvortrag" style="left:303px;top:0;width:303px;height:109px;background:linear-gradient(180deg,#e9ecef 0%,#b49f8c 55%,#5c4d44 100%);"></div>
  <div class="block block--navy" style="left:0;top:118px;width:303px;height:185px;"></div>
  <div class="stripe stripe--dark" style="top:92px;width:468px;"></div>
  <div class="stripe stripe--mid" style="top:100.5px;width:559px;"></div>
  <div class="stripe stripe--light" style="top:109px;width:387px;"></div>

  <div class="column column--light" style="left:56px;">
    <h2>Nutzen der <strong>Mitgliedschaft</strong></h2>
    <p>Lernen Sie aus den praktischen Erfahrungen der Mitglieder Teilen Sie ihre Erfahrungen, Benchmarken Sie Ihr Projektmanagement, Nutzen Sie die Bewertungen zur Einführung und Nutzen neuer Standards der agilen Szene, Industrie 4.0 für Ihr Unternehmen.</p>
    <p>Präsentieren Sie Ihr gewonnenes Wissen oder Ihres Unternehmens zum Nutzen der Mitglieder in Vorträgen und Workshops.</p>
    <p>Profitieren Sie von der ankerkannten VTR® – Ausbildung und nutzen Sie die Angebote, Best Practice und frühzeitig Potentiale zu nutzen. Lernen Sie interessante Firmen als zukünftige Arbeitgeber und Kollegen kennen!</p>
  </div>
  <div class="column column--dark" style="left:363px;">
    <h2>Wir brauchen <strong>Sie!</strong></h2>
    <p>Als Volunteer können Sie sich schon nebenbei erste Lorbeeren im professionellen Umfeld verdienen oder für sich ein neues Betätigungsfeld entdecken.</p>
    <p>Das VTR® Köln Chapter agiert wie ein Unternehmen, wir brauchen Experten, Rechtsabteilung, globale und lokale Führungskräfte, Marketing, Vertriebler, Botschafter, …</p>
    <p>Lassen Sie sich durch den Besuch der Veranstaltungen überzeugen. Mehr Informationen finden Sie auf unser Homepage.<br><strong>www.vtrnk.de</strong></p>
  </div>
</section>

</body>
</html>
```